Banners for website home page

I'm looking for 3 banners that will rotate on my website carousel addressing my 3 target markets. The website is Ledgerwise Harbor.

1) Young Starters
Headline: Start smart. Invest with confidence.
Sub: Learn the basics, set your first goal, and build a long-term plan with Ledgerwise Harbor.
CTA: Start free
Hero image ideas: Young person with phone/laptop; app UI overlay; subtle navy/gold chart shapes.

2) Saving for a Goal
Headline: Turn your goal into a plan.
Sub: Home deposit or child’s education—set targets, see projections, and track progress.
CTA: Plan my goal
Hero image ideas: Couple/family looking at house plans or a uni cap; progress bar overlay; warm light.

3) Retirement Fund Owners
Headline: Grow and protect your Retirement Fund.
Sub: Professional-grade tracking and signals to help your super grow—and last.
CTA: Start Now
Hero image ideas: Mature couple with tablet / beach walk; portfolio charts/compass motif overlaid.

Our app does the following:
Ledgerwise Harbor is an easy-to-use app designed to help everyday people take control of their investing journey.
Backed by over 10 years of proven investment models and experience, it empowers you to set realistic goals, build a tailored investment plan, and confidently manage your risk. With built-in education, alerts, and market insights, Ledgerwise Harbor helps you stay on course and maximise returns—no guesswork, just smart investing.

See attached an example AI generated banner and current logo to base colours, feel. for the website I use a dark blue menu and below would like a lighter colour - yellow/gold/white banner background.

Banner sizes : 1600 x 700 and 1200x525
Square size for mobile : 960x960 and 640x640
Format: WebP and PNG

```html
<!DOCTYPE html>
<html lang="en">
<head>
<meta charset="utf-8">
<title>Ledgerwise Harbor — Home Banners 1600x700</title>
<link href="https://fonts.googleapis.com/css2?family=Poppins:wght@400;600;700;800&display=swap" rel="stylesheet">
<style>
  :root{
    --board:#4d4d4d;
    --navy:#1b1f4b;
    --gold:#d8b155;
    --gold-deep:#c99a3a;
    --label-gold:#c9a24a;
    --white:#fcfcfc;
    --mist:#e7e7e7;
    --peach:#efd9b9;
  }
  *{box-sizing:border-box;margin:0;padding:0}
  html,body{width:717px;height:1200px;overflow:hidden;background:var(--board)}
  body{position:relative;font-family:"Poppins",Arial,sans-serif}
  .size-label{position:absolute;top:42px;left:0;width:717px;text-align:center;color:var(--label-gold);
    font-size:17px;font-weight:400;letter-spacing:9px}
  .banner{position:absolute;left:40px;width:637px;height:279px;overflow:hidden;
    box-shadow:0 18px 22px -10px rgba(0,0,0,.55)}
  .banner--starter{top:105px;background:var(--white)}
  .banner--goal{top:448px;background:linear-gradient(100deg,#274862 0%,#2c4d68 60%,#4a6a8f 100%)}
  .banner--retire{top:803px;background:var(--mist)}
  .art{position:absolute;inset:0}
  .copy{position:absolute;left:55px;top:54px}
  .headline{font-weight:600;color:var(--navy);font-size:27.5px;line-height:28.5px;letter-spacing:-.2px}
  .banner--goal .headline{color:#fff;font-size:29px;line-height:31px}
  .headline .accent{color:var(--gold)}
  .sub{margin-top:12px;color:var(--navy);font-size:12.4px;line-height:15.3px}
  .banner--goal .sub{color:#fff;line-height:16px;margin-top:10px}
  .banner--retire .sub{margin-top:10px;line-height:16px}
  .cta{position:absolute;left:52px;height:31px;border-radius:16px;background:var(--gold);
    color:var(--navy);font-weight:800;font-size:13.5px;display:flex;align-items:center;justify-content:center}
  .banner--starter .cta{top:215px;width:92px}
  .banner--goal .cta{top:186px;width:117px}
  .banner--retire .cta{top:202px;width:94px}
</style>
</head>
<body>
  <div class="size-label">1600 x 700</div>

  <section class="banner banner--starter">
    <svg class="art" width="637" height="279" viewBox="0 0 637 279">
      <defs>
        <linearGradient id="starterTint" x1="1" y1="0" x2="0" y2="0">
          <stop offset="0" stop-color="var(--peach)"/><stop offset=".6" stop-color="var(--peach)" stop-opacity=".75"/>
          <stop offset="1" stop-color="var(--peach)" stop-opacity="0"/></linearGradient>
        <linearGradient id="starterPhoto" x1="0" y1="0" x2="0" y2="1">
          <stop offset="0" stop-color="#5b4233"/><stop offset=".4" stop-color="#b8622e"/><stop offset="1" stop-color="#8a4a24"/></linearGradient>
        <linearGradient id="starterDevice" x1="0" y1="0" x2="0" y2="1">
          <stop offset="0" stop-color="#1f2226"/><stop offset=".7" stop-color="#2c2f35"/><stop offset="1" stop-color="#a8a8ac"/></linearGradient>
      </defs>
      <polygon points="480,0 637,0 637,279 560,279 600,200 560,120" fill="url(#starterTint)"/>
      <circle cx="443" cy="190" r="122" fill="var(--gold)"/>
      <rect x="562" y="6" width="35" height="35" fill="var(--gold)"/>
      <rect x="529" y="39" width="35" height="35" fill="var(--gold)"/>
      <g fill="var(--navy)">
        <circle cx="185" cy="211" r="2.8"/><circle cx="206" cy="211" r="2.8"/><circle cx="226" cy="211" r="2.8"/>
        <circle cx="247" cy="211" r="2.8"/><circle cx="268" cy="211" r="2.8"/><circle cx="288" cy="211" r="2.8"/>
        <circle cx="185" cy="248" r="2.8"/><circle cx="206" cy="248" r="2.8"/><circle cx="226" cy="248" r="2.8"/>
        <circle cx="247" cy="248" r="2.8"/><circle cx="268" cy="248" r="2.8"/><circle cx="288" cy="248" r="2.8"/>
      </g>
      <g role="img" aria-label="Smiling young man in an orange shirt holding a phone beside a laptop showing investment charts">
        <rect x="382" y="8" width="160" height="271" rx="10" fill="url(#starterPhoto)"/>
        <rect x="484" y="146" width="143" height="133" rx="6" fill="url(#starterDevice)"/>
      </g>
    </svg>
    <div class="copy">
      <h2 class="headline">Start smart.<br>Invest with<br>confidence.</h2>
      <p class="sub">Learn the basics, set your first goal,<br>and build a long-term plan with<br>Ledgerwise Harbor.</p>
    </div>
    <div class="cta">Start Free</div>
  </section>

  <section class="banner banner--goal">
    <svg class="art" width="637" height="279" viewBox="0 0 637 279">
      <defs><linearGradient id="goalPhoto" x1="0" y1="0" x2="0" y2="1">
        <stop offset="0" stop-color="#8fa6a0"/><stop offset=".5" stop-color="#c69b8a"/><stop offset="1" stop-color="#2e3f63"/></linearGradient></defs>
      <path d="M472 279 C472 190 540 112 637 112 L637 279 Z" fill="var(--gold)"/>
      <rect role="img" aria-label="Family of three sitting together, parents forming a roof with their arms, child holding house keys"
        x="347" y="38" width="240" height="197" rx="8" fill="url(#goalPhoto)"/>
      <polyline points="354,67 455,17 558,67" fill="none" stroke="var(--gold)" stroke-width="2"/>
      <g fill="var(--gold)">
        <circle cx="311" cy="136" r="2.6"/><circle cx="332" cy="136" r="2.6"/><circle cx="353" cy="136" r="2.6"/>
        <circle cx="373" cy="136" r="2.6"/><circle cx="394" cy="136" r="2.6"/><circle cx="415" cy="136" r="2.6"/>
        <circle cx="311" cy="173" r="2.6"/><circle cx="332" cy="173" r="2.6"/><circle cx="353" cy="173" r="2.6"/>
        <circle cx="373" cy="173" r="2.6"/><circle cx="394" cy="173" r="2.6"/><circle cx="415" cy="173" r="2.6"/>
      </g>
      <rect x="337" y="237" width="239" height="14" rx="7" fill="#fff"/>
      <rect x="341" y="240" width="231" height="8" rx="4" fill="#a9a9a9"/>
      <rect x="341" y="240" width="158" height="8" rx="4" fill="var(--gold-deep)"/>
    </svg>
    <div class="copy">
      <h2 class="headline">Turn your <span class="accent">goal</span><br>into a <span class="accent">plan.</span></h2>
      <p class="sub">Home deposit or child’s<br>education—set targets, see<br>projections, and track progress.</p>
    </div>
    <div class="cta">Plan my goal</div>
  </section>

  <section class="banner banner--retire">
    <svg class="art" width="637" height="279" viewBox="0 0 637 279">
      <defs><linearGradient id="retirePhoto" x1="0" y1="0" x2="1" y2="1">
        <stop offset="0" stop-color="#b9c8dc"/><stop offset=".55" stop-color="#ecc95d"/><stop offset="1" stop-color="#4c6a96"/></linearGradient></defs>
      <g stroke="#d2d2d2" stroke-width="1" fill="none">
        <polyline points="30,279 45,262 90,270 160,238 200,250 290,178 330,205 370,105 410,128 450,58 500,40 520,45 560,38 605,25 637,0"/>
        <line x1="180" y1="279" x2="180" y2="265"/><line x1="210" y1="279" x2="210" y2="258"/>
        <line x1="240" y1="279" x2="240" y2="245"/><line x1="270" y1="279" x2="270" y2="230"/>
        <line x1="300" y1="279" x2="300" y2="215"/><line x1="560" y1="279" x2="560" y2="90"/>
        <line x1="580" y1="279" x2="580" y2="75"/><line x1="600" y1="279" x2="600" y2="60"/>
        <line x1="620" y1="279" x2="620" y2="50"/>
      </g>
      <rect role="img" aria-label="Mature couple smiling while looking at a tablet together"
        x="345" y="15" width="238" height="264" rx="8" fill="url(#retirePhoto)"/>
      <g fill="var(--gold-deep)">
        <circle cx="491" cy="38" r="2.6"/><circle cx="512" cy="38" r="2.6"/><circle cx="533" cy="38" r="2.6"/>
        <circle cx="553" cy="38" r="2.6"/><circle cx="574" cy="38" r="2.6"/><circle cx="595" cy="38" r="2.6"/>
        <circle cx="491" cy="75" r="2.6"/><circle cx="512" cy="75" r="2.6"/><circle cx="533" cy="75" r="2.6"/>
        <circle cx="553" cy="75" r="2.6"/><circle cx="574" cy="75" r="2.6"/>
      </g>
      <g stroke="var(--gold-deep)" stroke-width="3.5">
        <line x1="337" y1="279" x2="598" y2="69"/>
        <line x1="390" y1="279" x2="563" y2="137"/>
      </g>
      <polygon points="607,62 590,64 603,79" fill="var(--gold-deep)"/>
      <polygon points="571,130 553,133 567,148" fill="var(--gold-deep)"/>
    </svg>
    <div class="copy">
      <h2 class="headline">Grow and protect<br>your Retirement<br>Fund</h2>
      <p class="sub">Professional-grade tracking and signals<br>to help your super grow—and last.</p>
    </div>
    <div class="cta">Start Now</div>
  </section>
</body>
</html>
```